Oil and Gas Exploration and Production company needs a business card design

We need a business card design using our logo and colors in the logo. We want a mainstream design.

```html
<!DOCTYPE html>
<html lang="en">
<head>
<meta charset="utf-8">
<title>Norvale Oil &amp; Gas – Business Card</title>
<link rel="stylesheet" href="https://fonts.googleapis.com/css2?family=Lato:wght@400;700;900&display=swap">
<style>
  :root {
    --backdrop: #2b2b2b;
    --card-white: #f7f7f7;
    --card-black: #0d0d0d;
    --gold: #c2952d;
    --text-white: #f2f2f2;
    --ink: #111111;
  }
  * { margin: 0; padding: 0; box-sizing: border-box; }
  html, body {
    width: 1200px; height: 997px; overflow: hidden;
    background: var(--backdrop);
    font-family: "Lato", Arial, sans-serif;
  }
  .card {
    position: absolute; left: 150px; top: 241px;
    width: 900px; height: 515px;
    background: var(--card-white);
    overflow: hidden;
    box-shadow: 0 18px 40px rgba(0,0,0,.5);
  }
  .card-wave { position: absolute; inset: 0; width: 900px; height: 515px; }
  .brand {
    position: absolute; left: 250px; top: 110px;
    display: flex; align-items: center; gap: 16px;
  }
  .brand-dot { width: 46px; height: 46px; border-radius: 50%; background: var(--gold); }
  .brand-name {
    font-weight: 900; font-size: 50px; color: var(--ink); letter-spacing: -.5px;
  }
  .holder { position: absolute; left: 62px; top: 350px; }
  .holder-name { font-weight: 900; font-size: 30px; color: var(--gold); }
  .holder-title { font-size: 16px; color: var(--text-white); margin-top: 2px; }
  .contacts { list-style: none; position: absolute; left: 62px; top: 420px; }
  .contacts li {
    display: flex; align-items: center; gap: 14px;
    font-size: 17px; color: var(--text-white); height: 28px;
  }
  .contacts svg { width: 20px; height: 20px; fill: var(--text-white); }
  .contacts .web { color: var(--gold); font-weight: 900; letter-spacing: 1.5px; }
  .address {
    position: absolute; left: 610px; top: 312px;
    font-size: 16px; line-height: 1.6; color: var(--text-white);
  }
</style>
</head>
<body>
  <section class="card" aria-label="Business card">
    <svg class="card-wave" viewBox="0 0 900 515" aria-hidden="true">
      <path fill="var(--gold)" d="M0,332 C130,270 260,282 430,312 C610,344 770,300 900,150 L900,515 L0,515 Z"/>
      <path fill="var(--card-black)" d="M0,346 C130,284 260,296 430,326 C610,358 770,316 900,168 L900,515 L0,515 Z"/>
    </svg>

    <div class="brand">
      <span class="brand-dot"></span>
      <span class="brand-name">Norvale Oil &amp; Gas</span>
    </div>

    <div class="holder">
      <h1 class="holder-name">Dana Halvorsen</h1>
      <p class="holder-title">Founder &amp; CEO</p>
    </div>

    <ul class="contacts">
      <li>
        <svg viewBox="0 0 24 24"><path d="M6.6 10.8a15 15 0 0 0 6.6 6.6l2.2-2.2c.3-.3.7-.4 1-.2 1.1.4 2.3.6 3.6.6.6 0 1 .4 1 1V20c0 .6-.4 1-1 1A17 17 0 0 1 3 4c0-.6.4-1 1-1h3.5c.6 0 1 .4 1 1 0 1.3.2 2.5.6 3.6.1.3 0 .7-.2 1z"/></svg>
        <span>555.014.2290</span>
      </li>
      <li>
        <svg viewBox="0 0 24 24"><path d="M2 5h20v14H2z M4 7v.5l8 5 8-5V7z" fill-rule="evenodd"/></svg>
        <span>d.halvorsen@norvale.com</span>
      </li>
      <li>
        <svg viewBox="0 0 24 24"><circle cx="12" cy="12" r="10"/><path d="M2 12h20M12 2c3 3 3 17 0 20M12 2c-3 3-3 17 0 20" stroke="var(--card-black)" stroke-width="1.5" fill="none"/></svg>
        <span class="web">www.norvale.com</span>
      </li>
    </ul>

    <address class="address" style="font-style:normal">
      2180 Harbor Ridge Blvd #410<br>
      Palm Meadow, Florida 33090
    </address>
  </section>
</body>
</html>
```